Hybrid education and entertainment company needs help with creating dynamic school worksheets

I'm looking for a skilled individual to create a versatile Microsoft Word template for school worksheets for Lessonvibe. Your task will involve:
- Designing a user-friendly and visually appealing template that can be easily customized for various subjects and grade levels.
- Ensuring the template includes sections for titles, instructions, questions, and space for student responses.
- Incorporating consistent formatting and styles to maintain a professional look across all worksheets.
- Adding placeholders for images, graphics, or interactive elements to enhance engagement.
- Testing the template to ensure compatibility and ease of use for educators.
Your work will help streamline the worksheet creation process, making it easier for educators to develop effective and engaging learning materials.

```html
<!DOCTYPE html>
<html lang="en">
<head>
<meta charset="utf-8">
<title>Lessonvibe Worksheet Template</title>
<link rel="stylesheet" href="https://fonts.googleapis.com/css2?family=Poppins:wght@400;600;700&display=swap">
<style>
  :root {
    --sky: #36c5f2;
    --ink: #111111;
    --paper: #ffffff;
    --backdrop: #f1f2f4;
    --rule: #8a8a8a;
  }
  * { margin: 0; padding: 0; box-sizing: border-box; }
  html, body {
    width: 1000px;
    height: 1200px;
    overflow: hidden;
    background: var(--backdrop);
    font-family: "Poppins", sans-serif;
    color: var(--ink);
  }
  .worksheet {
    position: absolute;
    left: 76px;
    top: 0;
    width: 848px;
    height: 1200px;
    background: var(--paper);
  }
  .worksheet > * { position: absolute; line-height: 1; white-space: nowrap; }

  .logo-place {
    left: 0; width: 100%; top: 122px;
    text-align: center;
    font-weight: 600; font-size: 30px;
    color: var(--sky);
  }
  .title-band {
    left: 0; top: 197px; width: 100%; height: 115px;
    background: var(--sky);
    display: flex; align-items: center; justify-content: center;
  }
  .title-band h1 {
    font-weight: 700; font-size: 70px; line-height: 1;
    color: var(--paper);
    letter-spacing: 1px; word-spacing: 14px;
    padding-top: 6px;
  }
  .section-tag {
    left: 109px; top: 355px; width: 230px; height: 60px;
    background: var(--sky);
    color: var(--paper);
    font-weight: 700; font-size: 29px;
    display: flex; align-items: center; justify-content: center;
    padding-top: 3px;
  }
  .instructions-text {
    left: 106px; top: 447px;
    font-size: 20px;
  }
  .section-heading {
    font-weight: 700; font-size: 32px;
    color: var(--sky);
  }
  .questions-heading { left: 100px; top: 520px; }
  .long-answer-heading { left: 102px; top: 843px; }

  .question-list { left: 102px; top: 0; list-style: none; }
  .question {
    position: absolute; left: 0;
    font-size: 14.5px; line-height: 1;
  }
  .question .num { position: absolute; left: 0; top: -2px; font-size: 13px; }
  .question .text { position: absolute; left: 48px; white-space: nowrap; }
  .q1 { top: 589px; } .q2 { top: 654px; } .q3 { top: 718px; } .q4 { top: 782px; }

  .image-placeholder {
    left: 513px; top: 557px; width: 231px; height: 246px;
    background: var(--sky);
    color: var(--paper);
    font-weight: 700; font-size: 30px;
    text-align: center;
  }
  .image-placeholder span { position: absolute; left: 0; width: 100%; }
  .image-placeholder .line-1 { top: 72px; }
  .image-placeholder .line-2 { top: 127px; }

  .answer-line {
    left: 104px; width: 642px; height: 0;
    border-top: 1px dotted var(--rule);
  }
  .answer-line.l1 { top: 914px; }
  .answer-line.l2 { top: 962px; }
  .answer-line.l3 { top: 1008px; }

  .tagline {
    left: 0; width: 100%; top: 1044px;
    text-align: center; font-size: 24px;
  }
  .page-number {
    left: 0; width: 100%; top: 1112px;
    text-align: center; font-size: 21px;
  }
</style>
</head>
<body>
  <main class="worksheet">
    <div class="logo-place">LOGO PLACE</div>

    <header class="title-band">
      <h1>WORKSHEET TITLE</h1>
    </header>

    <div class="section-tag">Instructions:</div>
    <p class="instructions-text">Lorem ipsum dolor sit amet, consectetur adipiscing elit,</p>

    <h2 class="section-heading questions-heading">Questions:</h2>
    <ol class="question-list">
      <li class="question q1"><span class="num">(1)</span><span class="text">Lorem ipsum dolor sit amet, consectetur ?</span></li>
      <li class="question q2"><span class="num">(2)</span><span class="text">Lorem ipsum dolor sit amet, consectetur ?</span></li>
      <li class="question q3"><span class="num">(3)</span><span class="text">Lorem ipsum dolor sit amet, consectetur ?</span></li>
      <li class="question q4"><span class="num">(4)</span><span class="text">Lorem ipsum dolor sit amet, consectetur ?</span></li>
    </ol>

    <div class="image-placeholder" role="img" aria-label="Placeholder for a worksheet image">
      <span class="line-1">Insert</span>
      <span class="line-2">IMAGE HERE</span>
    </div>

    <h2 class="section-heading long-answer-heading">Long Answer</h2>
    <div class="answer-line l1"></div>
    <div class="answer-line l2"></div>
    <div class="answer-line l3"></div>

    <p class="tagline">Engaging Learning Materials for All Grades</p>
    <p class="page-number">01</p>
  </main>
</body>
</html>
```